Real Estate Company Looking for Business Card Designs for 3 Executives

Hello!
Thanks so much for considering our project! We are a real estate investment company located in Edmonton, Alberta called Marlbeck Group of Companies. We invest/develop both commercial and residential real estate and are looking to create 3 DOUBLE-SIDED business cards for 3 top executives in the company! (for some reason it won't let us select the double-sided option, but yes, the cards are double sided and would be happy to tip extra)

We have certain guidelines that we want our business cards to for sure follow - the back of the Business card has to be the Black Background Version of the Logo which has already been designed and linked as a file (first file). We want the entire back of the card to simply just be the black background logo. In terms of the front of the card, would like to see a smaller version of the white background logo (linked as the second file) in the top left hand corner - of course, feel free to get creative and we can make revisions together along the way! and Then after that, just text. We want the card to be sharp, clean, easy on the eyes and highly professional looking. We would like the card to include the Full name of the Company (Marlbeck Group of Companies), Name of the Person, Title, Phone, Email. If possible please provide the front part of the card for 3 people:

1) Marlbeck Group of Companies, Lena Okafor, Chief Financial Officer, 780-555-0162, lenaokafor@marlbeckgroup.example

2) Marlbeck Group of Companies, Tobias Okafor, Chief Executive Officer, 780-555-0148, tobiasokafor@marlbeckgroup.example

3) Marlbeck Group of Companies, Rui Dalton, Chief Operations Officer, 587-555-0193, ruidalton@marlbeckgroup.example

Thank you so much for considering our project & we look forward to seeing your designs!

```html
<!DOCTYPE html>
<html lang="en">
<head>
<meta charset="utf-8">
<title>Marlbeck Group of Companies – Business Card</title>
<link rel="stylesheet" href="https://fonts.googleapis.com/css2?family=Jost:wght@300;400;500&family=Libre+Caslon+Text:wght@700&display=swap">
<style>
  :root {
    --backdrop: #ababab;
    --card-dark: #070304;
    --card-light: #ffffff;
    --ink: #0d0d0d;
    --ink-soft: #6d6d6d;
    --icon: #9a9a9a;
    --on-dark: #ffffff;
  }
  * { margin: 0; padding: 0; box-sizing: border-box; }
  html, body {
    width: 1200px; height: 1000px; overflow: hidden;
    background: radial-gradient(ellipse at center, #b3b3b3 0%, var(--backdrop) 70%);
    font-family: "Jost", sans-serif;
  }
  .card {
    position: absolute;
    left: 294px;
    width: 613px;
    height: 352px;
    border-radius: 22px;
    box-shadow: 0 24px 40px rgba(0,0,0,0.28), 0 6px 12px rgba(0,0,0,0.12);
  }
  .card--back { top: 82px; background: var(--card-dark); }
  .card--front { top: 545px; background: var(--card-light); color: var(--ink); }

  .wordmark {
    font-family: "Jost", sans-serif;
    font-weight: 400;
    text-transform: uppercase;
    display: flex; align-items: center;
  }
  .wordmark__mark { display: inline-block; }

  .card--back .wordmark {
    position: absolute; left: 0; right: 0; top: 0; bottom: 0;
    justify-content: center; gap: 16px;
    color: var(--on-dark);
    font-size: 34px; letter-spacing: 10px;
  }
  .card--back .wordmark__mark { width: 18px; height: 18px; background: var(--on-dark); }

  .card--front .wordmark {
    position: absolute; left: 37px; top: 50px;
    gap: 8px;
    color: var(--ink);
    font-size: 17px; letter-spacing: 3.5px;
  }
  .card--front .wordmark__mark { width: 10px; height: 10px; background: var(--ink); }

  .company {
    position: absolute; right: 36px; top: 47px;
    font-weight: 500; font-size: 25px; letter-spacing: 0.3px;
  }
  .person {
    position: absolute; right: 36px; top: 162px; text-align: right;
  }
  .person__name {
    font-family: "Libre Caslon Text", serif;
    font-weight: 700; font-size: 33px; line-height: 40px;
  }
  .person__title {
    font-weight: 300; font-size: 21px; color: var(--ink-soft); line-height: 28px;
  }
  .contact {
    position: absolute; right: 36px; top: 256px;
    list-style: none; text-align: right;
  }
  .contact__item {
    display: flex; justify-content: flex-end; align-items: center;
    font-weight: 300; font-size: 21px; line-height: 26px;
  }
  .contact__icon { width: 21px; height: 18px; margin-left: 12px; fill: var(--icon); }
</style>
</head>
<body>
  <section class="card card--back" aria-label="Card back">
    <div class="wordmark"><span class="wordmark__mark"></span>Marlbeck</div>
  </section>

  <section class="card card--front" aria-label="Card front">
    <div class="wordmark"><span class="wordmark__mark"></span>Marlbeck</div>
    <h1 class="company">Marlbeck Group of Companies</h1>
    <div class="person">
      <p class="person__name">Lena Okafor</p>
      <p class="person__title">Chief Financial Officer</p>
    </div>
    <ul class="contact">
      <li class="contact__item">780-555-0162
        <svg class="contact__icon" viewBox="0 0 24 24" aria-hidden="true"><path d="M6.6 10.8c1.4 2.8 3.8 5.1 6.6 6.6l2.2-2.2c.3-.3.7-.4 1-.2 1.1.4 2.3.6 3.6.6.6 0 1 .4 1 1V20c0 .6-.4 1-1 1C10.6 21 3 13.4 3 4c0-.6.4-1 1-1h3.5c.6 0 1 .4 1 1 0 1.3.2 2.5.6 3.6.1.3 0 .7-.2 1L6.6 10.8z"/></svg>
      </li>
      <li class="contact__item">lenaokafor@marlbeckgroup.example
        <svg class="contact__icon" viewBox="0 0 24 18" aria-hidden="true"><path d="M1 1h22v16H1z" fill="none" stroke="#9a9a9a" stroke-width="1.5"/><path d="M1 1l11 9 11-9M1 17l8-7M23 17l-8-7" fill="none" stroke="#9a9a9a" stroke-width="1.5"/></svg>
      </li>
    </ul>
  </section>
</body>
</html>
```